Email Signatures

I would like to create a new email signature for my team. The design will be the same for everyone, with only individual details such as name and email changing. You can also see our brand style on our website. https://www.tlmbespokehomes.com.au/

Target Market(s)

Clients for new builds or renovations

Industry/Entity Type

Construction

Colors

Designer to choose colors to be used in the design.

```html
<!DOCTYPE html>
<html lang="en">
<head>
<meta charset="utf-8">
<title>TLM Bespoke Homes – Email Signature</title>
<link rel="stylesheet" href="https://fonts.googleapis.com/css2?family=Montserrat:wght@500;600;700&display=swap">
<style>
  :root {
    --brand-green: #2f9e48;
    --brand-dark: #1c2424;
    --ink: #1a1f1f;
    --paper: #ffffff;
    --gold: #c9a24a;
    --silver: #b9bcbf;
    --charcoal: #2c3132;
    --orange: #e8922a;
  }
  * { margin: 0; padding: 0; box-sizing: border-box; }
  html, body { width: 1200px; height: 600px; overflow: hidden; background: var(--paper); }
  body { font-family: "Montserrat", Arial, sans-serif; color: var(--ink); }

  .signature { position: relative; width: 1200px; height: 600px; overflow: hidden; background: var(--paper); }
  .signature__shapes { position: absolute; inset: 0; }

  .brand {
    position: absolute; left: 48px; top: 84px;
    display: flex; align-items: center; gap: 12px;
    color: var(--paper); font-weight: 700; font-size: 20px; letter-spacing: 0.5px; white-space: nowrap;
  }
  .brand__mark { width: 18px; height: 18px; background: var(--brand-green); flex: none; }

  .person-name {
    position: absolute; left: 416px; top: 82px;
    font-size: 82px; font-weight: 700; letter-spacing: -1px; line-height: 1; color: var(--ink); white-space: nowrap;
  }
  .person-role {
    position: absolute; left: 420px; top: 196px;
    display: inline-block; padding-bottom: 10px; border-bottom: 3px solid var(--ink);
    font-size: 40px; font-weight: 600; line-height: 1; color: var(--ink); white-space: nowrap;
  }
  .person-role__lead { color: var(--brand-green); font-weight: 700; }

  .contact-list { position: absolute; left: 580px; top: 272px; list-style: none; }
  .contact-list__item {
    display: flex; align-items: center; gap: 26px;
    height: 54px; font-size: 26px; font-weight: 500; color: var(--ink); white-space: nowrap;
  }
  .contact-list__icon { width: 30px; height: 30px; flex: none; }
</style>
</head>
<body>
<main class="signature">
  <svg class="signature__shapes" width="1200" height="600" viewBox="0 0 1200 600">
    <defs>
      <linearGradient id="roomTones" x1="0" y1="0" x2="1" y2="1">
        <stop offset="0" stop-color="#f5f5f3"/>
        <stop offset="0.6" stop-color="#d9dbd7"/>
        <stop offset="1" stop-color="#b9a98e"/>
      </linearGradient>
      <linearGradient id="portraitTones" x1="0" y1="0" x2="0" y2="1">
        <stop offset="0" stop-color="#e7e9ea"/>
        <stop offset="1" stop-color="#2b3440"/>
      </linearGradient>
      <linearGradient id="fadeRoom" x1="0" y1="0" x2="1" y2="0">
        <stop offset="0.55" stop-color="#ffffff" stop-opacity="0"/>
        <stop offset="1" stop-color="#ffffff" stop-opacity="1"/>
      </linearGradient>
    </defs>

    <rect x="0" y="0" width="440" height="600" fill="url(#roomTones)" role="img" aria-label="Bright modern home interior backdrop"/>
    <rect x="0" y="0" width="440" height="600" fill="url(#fadeRoom)"/>

    <polygon points="0,0 400,0 310,200 0,200" fill="var(--brand-dark)"/>
    <polygon points="400,0 435,0 345,200 310,200" fill="var(--brand-green)"/>

    <polygon points="1060,0 1200,0 1200,90" fill="var(--brand-green)"/>
    <polygon points="1110,0 1200,0 1200,56" fill="var(--brand-dark)"/>

    <polygon points="860,600 1200,380 1200,600" fill="var(--brand-green)"/>
    <polygon points="905,600 1200,420 1200,600" fill="var(--brand-dark)"/>

    <circle cx="300" cy="345" r="146" fill="var(--brand-green)"/>
    <circle cx="300" cy="345" r="138" fill="var(--paper)"/>
    <circle cx="300" cy="345" r="128" fill="url(#portraitTones)" role="img" aria-label="Portrait photo of the team member"/>

    <line x1="558" y1="262" x2="558" y2="500" stroke="var(--ink)" stroke-width="2"/>

    <g class="badges">
      <circle cx="378" cy="545" r="34" fill="var(--gold)"/>
      <circle cx="483" cy="545" r="34" fill="var(--charcoal)"/>
      <circle cx="588" cy="545" r="34" fill="var(--silver)"/>
      <circle cx="693" cy="545" r="34" fill="var(--charcoal)"/>
      <circle cx="798" cy="545" r="34" fill="var(--silver)"/>
      <circle cx="903" cy="545" r="34" fill="var(--orange)"/>
      <circle cx="1008" cy="545" r="34" fill="var(--charcoal)"/>
      <circle cx="1113" cy="545" r="34" fill="var(--silver)"/>
    </g>
  </svg>

  <div class="brand"><span class="brand__mark"></span>TLM Bespoke Homes</div>

  <h1 class="person-name">Daniel Whitford</h1>
  <p class="person-role"><span class="person-role__lead">Construction</span> Manager</p>

  <ul class="contact-list">
    <li class="contact-list__item">
      <svg class="contact-list__icon" viewBox="0 0 24 24"><path fill="var(--ink)" d="M6.6 10.8a15.1 15.1 0 0 0 6.6 6.6l2.2-2.2a1 1 0 0 1 1-.25 11.4 11.4 0 0 0 3.6.57 1 1 0 0 1 1 1V20a1 1 0 0 1-1 1A17 17 0 0 1 3 4a1 1 0 0 1 1-1h3.5a1 1 0 0 1 1 1c0 1.25.2 2.45.57 3.57a1 1 0 0 1-.25 1z"/></svg>
      0412 555 019
    </li>
    <li class="contact-list__item">
      <svg class="contact-list__icon" viewBox="0 0 24 24" fill="none" stroke="var(--ink)" stroke-width="2"><circle cx="12" cy="12" r="9"/><path d="M3 12h18M12 3c3 3.5 3 14.5 0 18M12 3c-3 3.5-3 14.5 0 18"/></svg>
      tlmbespokehomes.com.au
    </li>
    <li class="contact-list__item">
      <svg class="contact-list__icon" viewBox="0 0 24 24"><path fill="var(--ink)" d="M3 5h18v14H3z"/><path d="M3 6l9 7 9-7" fill="none" stroke="var(--paper)" stroke-width="2"/></svg>
      daniel@tlmbespokehomes.com.au
    </li>
    <li class="contact-list__item">
      <svg class="contact-list__icon" viewBox="0 0 24 24"><path fill="var(--ink)" d="M12 2a7 7 0 0 0-7 7c0 5.2 7 13 7 13s7-7.8 7-13a7 7 0 0 0-7-7zm0 9.5A2.5 2.5 0 1 1 12 6.5a2.5 2.5 0 0 1 0 5z"/></svg>
      2/7 Banksia Place, Seaford
    </li>
  </ul>
</main>
</body>
</html>
```